Flyer-Design für Naturkosmetik und Wellness
Zielgruppe
Naturkosmetik und Wellness
Aufgabenstellung
Das Design soll schlicht sein , aber nicht unscheinbar wirken. Ich möchte die Flyer gerne als Postkarte vorne und hinten gestaltet.
Vorderseite : Mein Name im gleichen Design , wie bei meinen Visitenkarten.Text:Kosmetik und Entspannung im Einklang mit der Natur .
Rückseite : Termine nach Vereinbarung Mo 16.00 h- 19.00h , Mi und Do 15.00h - 19.00h und Fr 14.00h - 18.00h

```html
<!DOCTYPE html>
<html lang="de">
<head>
<meta charset="utf-8">
<title>Petra Wolken – Flyer</title>
<link href="https://fonts.googleapis.com/css2?family=Raleway:wght@300;400;700&family=Quicksand:wght@400&display=swap" rel="stylesheet">
<style>
  :root{
    --taupe:#85766a;
    --taupe-line:#9c8c80;
    --beige:#d8c6b2;
    --beige-deep:#bfa996;
    --ink-soft:#8b8580;
    --accent:#a5897a;
    --copy:#aea29a;
    --white:#ffffff;
  }
  *{margin:0;padding:0;box-sizing:border-box}
  html,body{width:1200px;height:570px;overflow:hidden;background:var(--white)}
  .sheet{position:relative;width:1200px;height:570px}
  .card{position:absolute;top:36px;width:350px;height:494px;overflow:hidden;background:var(--white);
        box-shadow:3px 4px 6px rgba(0,0,0,.35);border:1px solid #e4e0dc}
  .card--front-a{left:37px}
  .card--back{left:424px}
  .card--front-b{left:812px;background:linear-gradient(180deg,#ffffff 0%,#eee5dc 25%,#d3c1ae 55%,#c4b09c 80%)}
  .shape{position:absolute;left:0;top:0;width:350px;height:494px}
  .tagline{position:absolute;left:0;right:0;text-align:center;font-family:"Quicksand",sans-serif;
           font-size:12px;letter-spacing:1.6px;color:var(--ink-soft)}
  .tagline .dot{display:inline-block;width:4px;height:4px;border-radius:50%;background:var(--ink-soft);
           margin:0 9px;vertical-align:middle}
  .card--front-a .tagline{top:24px}
  .card--front-b .tagline{top:16px}
  .artwork{position:absolute}
  .card--front-a .artwork{left:45px;top:55px;width:262px;height:250px;border-radius:42% 38% 40% 44%/38% 42% 46% 40%;
           background:linear-gradient(135deg,#e9d6bd 0%,#cdb8a2 55%,#ad9c8c 100%)}
  .card--front-b .artwork{left:60px;top:57px;width:250px;height:248px;border-radius:30px;
           background:linear-gradient(180deg,rgba(255,255,255,.75) 0%,rgba(226,212,197,.6) 100%)}
  .headline{position:absolute;left:0;right:0;text-align:center;color:var(--white);font-family:"Raleway",sans-serif}
  .headline strong{display:block;font-weight:700;font-size:21.5px;line-height:27px}
  .headline span{display:block;font-weight:400;font-size:21.5px;line-height:27px}
  .card--front-a .headline,.card--front-b .headline{top:376px}
  .web{position:absolute;left:0;right:0;text-align:center;font-family:"Raleway",sans-serif;font-weight:700;
       font-size:13px;letter-spacing:1.2px}
  .card--front-a .web,.card--front-b .web{top:460px;color:var(--white)}
  .card--back .web{top:462px;color:var(--accent)}
  .brand-name{position:absolute;left:0;right:0;top:70px;text-align:center;font-family:"Raleway",sans-serif;
       font-weight:300;font-size:40px;color:var(--white);letter-spacing:1px}
  .info{position:absolute;left:0;right:0;text-align:center;font-family:"Raleway",sans-serif;
       font-size:13.5px;line-height:19px;color:var(--copy)}
  .info h2{font-size:13.5px;font-weight:700;color:var(--accent);line-height:21px}
  .info--hours{top:205px}
  .info--contact{top:306px}
</style>
</head>
<body>
<main class="sheet">

  <section class="card card--front-a">
    <p class="tagline">ankommen<i class="dot"></i>wohlfühlen<i class="dot"></i>entspannen</p>
    <div class="artwork" role="img" aria-label="Illustration einer entspannten Frau mit Handtuch-Turban, Kerze und Blüte auf beigem Farbfeld"></div>
    <svg class="shape" viewBox="0 0 350 494" aria-hidden="true">
      <path d="M0 390 C30 300 120 330 200 332 C270 334 320 320 350 305 L350 494 L0 494 Z" fill="var(--taupe)"/>
      <path d="M42 336 C110 310 200 330 260 331 C300 332 325 322 334 317" fill="none" stroke="var(--taupe-line)" stroke-width="1.2"/>
    </svg>
    <div class="headline"><strong>Kosmetik &amp; Entspannung</strong><span>im Einklang mit der Natur</span></div>
    <p class="web">www.ruhezeit-kosmetik.de</p>
  </section>

  <section class="card card--back">
    <svg class="shape" viewBox="0 0 350 494" aria-hidden="true">
      <path d="M0 0 H350 V108 C320 135 260 142 200 136 C140 130 80 115 40 130 L0 147 Z" fill="var(--taupe)"/>
      <path d="M42 138 C80 122 140 126 200 141 C260 150 310 140 332 128" fill="none" stroke="var(--taupe-line)" stroke-width="1.2"/>
    </svg>
    <p class="brand-name">Petra Wolken</p>
    <div class="info info--hours">
      <h2>Termine nach Vereinbarung</h2>
      <p>Mo 16.00h - 19.00h</p>
      <p>Mi und Do 15.00h - 19.00h</p>
      <p>Fr 14.00h - 18.00h</p>
    </div>
    <div class="info info--contact">
      <h2>Petra Wolken</h2>
      <p>Lindenweg 12</p>
      <p>73100 Musterstadt</p>
      <p>petra@ruhezeit-kosmetik.de</p>
      <p>Tel. 0151 000 123 45</p>
    </div>
    <p class="web">www.ruhezeit-kosmetik.de</p>
  </section>

  <section class="card card--front-b">
    <p class="tagline">ankommen<i class="dot"></i>wohlfühlen<i class="dot"></i>entspannen</p>
    <div class="artwork" role="img" aria-label="Illustration einer entspannten Frau mit Handtuch-Turban, Kerze und Blüte"></div>
    <svg class="shape" viewBox="0 0 350 494" aria-hidden="true">
      <path d="M0 390 C30 300 120 330 200 332 C270 334 320 320 350 305 L350 494 L0 494 Z" fill="var(--taupe)"/>
      <path d="M42 336 C110 310 200 330 260 331 C300 332 325 322 334 317" fill="none" stroke="#ffffff" stroke-opacity=".7" stroke-width="1.2"/>
    </svg>
    <div class="headline"><strong>Kosmetik &amp; Entspannung</strong><span>im Einklang mit der Natur</span></div>
    <p class="web">www.ruhezeit-kosmetik.de</p>
  </section>

</main>
</body>
</html>
```